Brightwater Valley Strong Unions and Households Initiative-Postcard

We need a postcard to promote our program. We will use the postcard to remind clients of appointments or even use it as a marketing tool when we go out to events. We provide healthy relationship education, financial classes and job readiness education. Our target population is adult couples. Mostly Spanish speaking. If its possible to incorporate all three components into the design that would be great, if not, healthy relationship would be our priority.

Attached is a logo we would like to use.

I have also included the text we would like to use. Would you please make all text editable incase we want to add different text.

The funding statement has to go at the bottom (it can be in small text).

Industry/Entity Type

Marketing

Requirements
Must have
• if you use images of people, please use Latino images. Our target population is Spanish speaking.

```html
<!DOCTYPE html>
<html lang="es">
<head>
<meta charset="utf-8">
<title>Brightwater Valley Strong Unions and Households Initiative – Postcard</title>
<link href="https://fonts.googleapis.com/css2?family=Open+Sans:wght@400;600;700&display=swap" rel="stylesheet">
<style>
  :root{
    --navy:#0f2a4f;
    --orange:#f39322;
    --ink:#3a3a3a;
    --muted:#5c5c5c;
    --rule:#b9b9b9;
    --paper:#ffffff;
    --stage:#ececec;
    --photo-b:#d9c2ae;
    --photo-c:#e8dfd6;
  }
  *{box-sizing:border-box;margin:0;padding:0}
  html,body{width:929px;height:1200px;overflow:hidden}
  body{background:var(--stage);font-family:"Open Sans",Arial,sans-serif;position:relative}
  .postcard{position:absolute;left:138px;width:636px;height:493px;background:var(--paper);overflow:hidden;box-shadow:0 2px 6px rgba(0,0,0,.18)}
  .postcard--front{top:82px}
  .postcard--back{top:626px}
  .postcard__art{position:absolute;inset:0;width:636px;height:493px}
  .brand{position:absolute;left:18px;top:72px;display:flex;align-items:center;gap:7px}
  .brand__dot{width:16px;height:16px;border-radius:50%;background:var(--orange);flex:none}
  .brand__name{font-weight:600;font-size:17px;color:var(--orange);white-space:nowrap}
  .slogan{position:absolute;color:var(--navy);font-weight:600}
  .postcard--front .slogan{left:0;width:238px;top:138px;text-align:center;font-size:16px;line-height:25px}
  .postcard--back .slogan{left:30px;top:134px;font-size:14px}
  .services{position:absolute;left:0;top:211px;width:238px;height:120px;background:var(--orange);padding:10px 0 0 18px;color:#fff}
  .services__title{font-weight:700;font-size:18px;margin-bottom:5px}
  .services__item{display:flex;align-items:center;gap:8px;font-size:15px;line-height:26px}
  .services__item svg{flex:none}
  .partner{position:absolute;display:flex;align-items:center;gap:6px;color:var(--navy);font-weight:700;font-size:13px;line-height:15px}
  .partner__mark{width:18px;height:18px;background:#c8304c;flex:none}
  .postcard--front .partner{left:52px;top:365px;width:150px}
  .postcard--back .partner{left:26px;top:306px;width:130px}
  .callout{position:absolute;left:0;right:0;bottom:14px;display:flex;justify-content:center;align-items:center;gap:10px;color:#fff;font-size:16px}
  .callout__phone{display:flex;align-items:center;gap:6px}
  .program{position:absolute;left:15px;top:157px;width:318px;font-size:10.5px;line-height:13.5px;color:var(--muted)}
  .program__title{color:var(--orange);font-weight:600}
  .photo{position:absolute;left:158px;top:254px;width:190px;height:126px;background:linear-gradient(135deg,var(--photo-c),var(--photo-b));border-radius:2px}
  .funding{position:absolute;left:15px;top:386px;width:330px;font-size:7.5px;line-height:9.5px;color:var(--ink)}
  .return-address{position:absolute;left:358px;top:24px;width:150px;font-size:10.5px;line-height:14px;color:var(--muted)}
  .stamp-box{position:absolute;left:519px;top:23px;width:99px;height:61px;border:1.5px solid var(--rule)}
  .address-line{position:absolute;left:405px;width:216px;height:1.5px;background:var(--rule)}
</style>
</head>
<body>

<section class="postcard postcard--front" aria-label="Postcard front">
  <svg class="postcard__art" viewBox="0 0 636 493" aria-hidden="true">
    <defs>
      <linearGradient id="couplePhoto" x1="0" y1="0" x2="1" y2="1">
        <stop offset="0" stop-color="#9fb27c"/>
        <stop offset=".55" stop-color="#d7bda5"/>
        <stop offset="1" stop-color="#ece4dc"/>
      </linearGradient>
    </defs>
    <path role="img" aria-label="Photo of a smiling Latino couple embracing outdoors" d="M352 0H636V450H275C235 330 255 110 352 0Z" fill="url(#couplePhoto)"/>
    <path d="M352 0C255 110 235 330 275 450" fill="none" stroke="var(--orange)" stroke-width="11"/>
    <path d="M0 440Q318 392 636 440V493H0Z" fill="#fff"/>
    <path d="M0 447Q318 400 636 447V493H0Z" fill="var(--navy)"/>
  </svg>

  <div class="brand"><span class="brand__dot"></span><span class="brand__name">Uniones y Hogares Fuertes</span></div>
  <p class="slogan">…porque una relación<br>sana está a su alcance</p>

  <div class="services">
    <p class="services__title">WE PROVIDE...</p>
    <p class="services__item"><svg width="13" height="13" viewBox="0 0 13 13"><circle cx="6.5" cy="6.5" r="5.5" fill="none" stroke="#fff" stroke-width="1.4"/><path d="M5.3 4l2.5 2.5-2.5 2.5" fill="none" stroke="#fff" stroke-width="1.4"/></svg>HEALTHY RELATIONSHIP</p>
    <p class="services__item"><svg width="13" height="13" viewBox="0 0 13 13"><circle cx="6.5" cy="6.5" r="5.5" fill="none" stroke="#fff" stroke-width="1.4"/><path d="M5.3 4l2.5 2.5-2.5 2.5" fill="none" stroke="#fff" stroke-width="1.4"/></svg>FINANCIAL CLASSES</p>
    <p class="services__item"><svg width="13" height="13" viewBox="0 0 13 13"><circle cx="6.5" cy="6.5" r="5.5" fill="none" stroke="#fff" stroke-width="1.4"/><path d="M5.3 4l2.5 2.5-2.5 2.5" fill="none" stroke="#fff" stroke-width="1.4"/></svg>JOB READINESS</p>
  </div>

  <div class="partner"><span class="partner__mark"></span><span>Valley Neighbors Alliance</span></div>

  <p class="callout">Para más información, llame a
    <span class="callout__phone"><svg width="16" height="16" viewBox="0 0 16 16"><circle cx="8" cy="8" r="7" fill="none" stroke="#fff" stroke-width="1.3"/><path d="M5.6 4.6l1.2 1.5-.7.9c.4.9 1.1 1.6 2 2l.9-.7 1.5 1.2-.7 1.2c-2.5-.3-4.6-2.4-4.9-4.9z" fill="#fff"/></svg>555-210-4830</span>
  </p>
</section>

<section class="postcard postcard--back" aria-label="Postcard back">
  <svg class="postcard__art" viewBox="0 0 636 493" aria-hidden="true">
    <path d="M284 0Q379 170 379 450" fill="none" stroke="#e2e2e2" stroke-width="6"/>
    <path d="M291 0Q386 170 386 450" fill="none" stroke="var(--orange)" stroke-width="8"/>
    <path d="M0 440Q318 392 636 440V493H0Z" fill="#fff"/>
    <path d="M0 447Q318 400 636 447V493H0Z" fill="var(--navy)"/>
  </svg>

  <div class="brand"><span class="brand__dot"></span><span class="brand__name">Uniones y Hogares Fuertes</span></div>
  <p class="slogan">…porque una relación sana está a su alcance</p>

  <div class="program">
    <p class="program__title">Brightwater Valley Strong Unions and Households (BV-SUH)</p>
    <p>Healthy Relationships Workshops for Adult Couples and Youth Adult Couples Topics: safe communication skills, effective problem solving, commitment, loving style, and much more! Youth Topics: self-esteem, recognizing signs of abuse, healthy relationships, safety planning and additional resources.</p>
  </div>

  <div class="photo" role="img" aria-label="Photo of a happy Latino family with a child on the father's shoulders"></div>

  <div class="partner"><span class="partner__mark"></span><span>Valley Neighbors Alliance</span></div>

  <p class="funding">Funding for this project was provided by the National Family Services Agency, Office of Household Support, Grant: #47BV2291. These services are available to all eligible persons, regardless of race, gender, age, disability, or religion.</p>

  <p class="return-address">Brightwater Valley Strong Unions and Households Initiative<br>(555) 318-2640, Ext. 2150</p>
  <div class="stamp-box"></div>
  <div class="address-line" style="top:190px"></div>
  <div class="address-line" style="top:224px"></div>
  <div class="address-line" style="top:261px"></div>

  <p class="callout">Para más información, llame a
    <span class="callout__phone"><svg width="16" height="16" viewBox="0 0 16 16"><circle cx="8" cy="8" r="7" fill="none" stroke="#fff" stroke-width="1.3"/><path d="M5.6 4.6l1.2 1.5-.7.9c.4.9 1.1 1.6 2 2l.9-.7 1.5 1.2-.7 1.2c-2.5-.3-4.6-2.4-4.9-4.9z" fill="#fff"/></svg>555-210-4830</span>
  </p>
</section>

</body>
</html>
```